Aviation: IFR Study Guide Book Cover

We need a book cover (front and back) designed for an Instrument Flight Rules (IFR) study guide used by helicopter and airplane pilots to obtain an instrument rating for a helicopter or airplane. Below is the title and subtitles.

TITLE: IFR STUDY GUIDE
SUBTITLE 1: Checkride Preparation for Airplane and Helicopter Pilots
SUBTITLE 2: Prepare for your Instrument Rating with Confidence

We have also upload recommended text to be included on the back cover. In addition, we included images of similar book covers that we like and ones that we do not like. Below are links to two others books by the author.

https://www.shopvendrix.com/Rotorcraft-Exam-Handbook-oral-flighttest/dp/204715382K
https://www.shopvendrix.com/Manual-Floatcraft-Piloting-Marcus-Holloway/dp/1702538146

Target Market(s)

Flight students

Industry/Entity Type

Aviation

Requirements
Nice to have
• helicopter and airplane

```html
<!DOCTYPE html>
<html lang="en">
<head>
<meta charset="utf-8">
<title>IFR Study Guide – Cover Spread</title>
<link rel="stylesheet" href="https://fonts.googleapis.com/css2?family=Bebas+Neue&family=Comfortaa:wght@400;500;600&family=Arimo:wght@400&display=swap">
<style>
  :root {
    --orange: #ff7200;
    --black: #000000;
    --white: #ffffff;
    --ink: #111111;
    --photo-light: #f4f5f7;
    --photo-mid: #9a9ca3;
    --photo-dark: #2a2b30;
  }
  html, body { margin: 0; padding: 0; overflow: hidden; background: var(--white); }
  .spread {
    position: relative; width: 1200px; height: 849px; overflow: hidden;
    background: var(--black);
  }
  .top-band { position: absolute; left: 0; top: 0; width: 1200px; height: 45px; background: var(--orange); }
  .spine-gap { position: absolute; left: 600px; top: 0; width: 2px; height: 849px; background: var(--white); }

  /* Back cover */
  .back { position: absolute; left: 0; top: 0; width: 600px; height: 849px; }
  .back-blurb { position: absolute; left: 0; top: 45px; width: 600px; height: 412px; background: var(--black); }
  .back-author { position: absolute; left: 2px; top: 457px; width: 598px; height: 392px; background: var(--orange); }
  .section-heading {
    position: absolute; left: 0; width: 600px; text-align: center; margin: 0;
    font-family: "Comfortaa", sans-serif; font-weight: 500; font-size: 14.5px; color: var(--orange);
  }
  .copy { position: absolute; left: 53px; width: 481px; font-family: "Arimo", Arial, sans-serif; font-size: 10.2px; }
  .copy .line { height: 30.3px; line-height: 14px; white-space: nowrap; text-align: justify; text-align-last: justify; }
  .copy .line.last { text-align-last: left; }
  .copy--light { color: var(--white); }
  .copy--dark { color: var(--ink); }
  .topics { position: absolute; left: 0; top: 0; font-family: "Arimo", Arial, sans-serif; font-size: 10.2px; color: var(--white); }
  .topic { position: absolute; white-space: nowrap; }
  .topic::before { content: "•"; color: var(--orange); font-size: 6px; margin-right: 3px; vertical-align: 1px; }
  .author-heading {
    position: absolute; left: 53px; top: 480px; margin: 0;
    font-family: "Comfortaa", sans-serif; font-weight: 500; font-size: 17px; color: var(--ink);
  }

  /* Front cover */
  .front { position: absolute; left: 602px; top: 45px; width: 598px; height: 804px; background: var(--black); }
  .title {
    position: absolute; left: 30px; top: 48px; margin: 0; width: 540px; white-space: nowrap;
    font-family: "Bebas Neue", Impact, sans-serif; font-size: 107px; line-height: 1; letter-spacing: 1px;
    color: var(--orange);
  }
  .subtitle {
    position: absolute; left: 0; top: 160px; width: 598px; margin: 0; text-align: center;
    font-family: "Comfortaa", sans-serif; font-weight: 500; font-size: 24.5px; line-height: 39px; color: var(--white);
  }
  .tagline {
    position: absolute; left: 0; top: 246px; width: 598px; margin: 0; text-align: center;
    font-family: "Comfortaa", sans-serif; font-size: 20.5px; color: var(--orange);
  }
  .cover-art {
    position: absolute; left: 0; top: 326px; width: 598px; height: 428px;
    background: linear-gradient(100deg, var(--photo-light) 0%, var(--photo-light) 30%, var(--photo-mid) 58%, var(--photo-dark) 85%);
  }
  .author-name {
    position: absolute; left: 0; top: 763px; width: 598px; margin: 0; text-align: center;
    font-family: "Comfortaa", sans-serif; font-weight: 500; font-size: 20.5px; color: var(--orange);
  }
</style>
</head>
<body>
<div class="spread">
  <div class="top-band"></div>

  <section class="back">
    <div class="back-blurb"></div>
    <div class="back-author"></div>

    <h2 class="section-heading" style="top:58px;">Prepare for your IFR check ride with confidence</h2>
    <div class="copy copy--light" style="top:95px;">
      <div class="line">Becoming an instrument rated pilot is one of the most challenging ratings to obtain.&nbsp; This guide helps</div>
      <div class="line">prepare you to pass your IFR check ride with confidence.&nbsp; The question-and-answer format is easy to</div>
      <div class="line last">follow and provides detailed explanations for expanded knowledge.</div>
    </div>

    <h2 class="section-heading" style="top:190px;">Includes Helicopter and Airplane Specific Content</h2>
    <div class="copy copy--light" style="top:226px;">
      <div class="line">This guide is designed to prepare an airplane or helicopter pilot the oral portion of the IFR checkride.</div>
      <div class="line">Unlike other resources, this guide specifically addresses the&nbsp; differences with IFR flight in helicopters.</div>
      <div class="line">As a dual rated pilot, the author ensures to identify areas of differences between the two categories of</div>
      <div class="line last">IFR flight.&nbsp;&nbsp; The following concepts are addressed within the guide.</div>
    </div>

    <ul class="topics">
      <li class="topic" style="left:53px;top:352px;">Preflight Actions</li>
      <li class="topic" style="left:218px;top:352px;">Enroute Procedures</li>
      <li class="topic" style="left:389px;top:352px;">Aeromedical Factors</li>
      <li class="topic" style="left:52px;top:385px;">General IFR Concepts</li>
      <li class="topic" style="left:217px;top:384px;">Approach Procedures</li>
      <li class="topic" style="left:388px;top:385px;">Weather Fundamentals</li>
      <li class="topic" style="left:51px;top:420px;">Departure Procedures</li>
      <li class="topic" style="left:218px;top:420px;">IFR Emergencies</li>
      <li class="topic" style="left:387px;top:420px;">Risk Management</li>
    </ul>

    <h2 class="author-heading">About the Author</h2>
    <div class="copy copy--dark" style="top:525px;">
      <div class="line">Marcus Holloway is ATP rated pilot and helicopter and fixed-wing instructor.&nbsp; Marcus is the owner and operator</div>
      <div class="line">Keel Ridge, LLC which does business as Rotor Aviation and Gull Aviation.&nbsp; Rotor Aviation provides</div>
      <div class="line">primary helicopter flight instruction while Gull Aviation provides seaplane flight instruction and tours.</div>
      <div class="line">In addition to instructing, Marcus has authored other books to include The Rotorcraft Exam Handbook, and</div>
      <div class="line">Manual of Floatcraft Piloting.&nbsp; Marcus lives in Kentucky with his beautiful wife Dana.&nbsp; They have a daughter,</div>
      <div class="line">Claire, that is dual rated and employed as a captain for a charter company.&nbsp;&nbsp; Prior to learning to fly, Marcus</div>
      <div class="line">spent several years in the military as a Special Warfare Combat Craft Crewman in the U.S. Navy and</div>
      <div class="line last">Ranger-qualified infantry officer in the U.S. Army.</div>
    </div>
  </section>

  <div class="spine-gap"></div>

  <section class="front">
    <h1 class="title">IFR STUDY GUIDE</h1>
    <p class="subtitle">Checkride Preparation for Airplane<br>and Helicopter Pilots</p>
    <p class="tagline">Prepare for your Instrument Rating with Confidence</p>
    <div class="cover-art" role="img" aria-label="Enroute IFR navigation chart blending into a helicopter instrument panel over a city seen from above"></div>
    <p class="author-name">Marcus Holloway</p>
  </section>
</div>
</body>
</html>
```